Need a simple buisness card for my plumbing business. Would like it to be black background with white text.

Industry/Entity Type

Business

Requirements
Must have
• On the front of the card I need to have,
TKB PLUMBING SERVICES
PLUMBERS, DRAINERS & GASFITTERS
Dorian Wellsby
0471596083
Info@tkbplumbingservices.com.au
LIC No 517483f
ABN No 61907354218
On the back I need in point form
Domestic,industrial,commercial, all new installations, renovations, sewer renewals, repairs,
Fully licensed and insured
Nice to have
• A nice simple logo

```html
<!DOCTYPE html>
<html lang="en">
<head>
<meta charset="utf-8">
<title>TKB Plumbing Services – Business Card</title>
<link rel="stylesheet" href="https://fonts.googleapis.com/css2?family=Montserrat:wght@400&display=swap">
<style>
  :root {
    --page-bg: #d8d2ca;
    --card-bg: #050505;
    --card-sheen: #1a1a1a;
    --ink: #f2f2f2;
  }
  * { box-sizing: border-box; margin: 0; padding: 0; }
  html, body {
    width: 1200px;
    height: 900px;
    overflow: hidden;
    background: var(--page-bg);
  }
  body {
    display: flex;
    flex-direction: column;
    align-items: center;
    justify-content: center;
    gap: 40px;
    font-family: "Montserrat", "Arial", sans-serif;
    font-weight: 400;
    color: var(--ink);
  }
  .card {
    position: relative;
    width: 680px;
    height: 388px;
    background: linear-gradient(160deg, var(--card-sheen) 0%, var(--card-bg) 45%, var(--card-bg) 100%);
    overflow: hidden;
    box-shadow: 0 6px 18px rgba(0, 0, 0, 0.25);
  }
  .card__header {
    position: absolute;
    top: 34px;
    left: 38px;
    line-height: 1.2;
    color: var(--ink);
  }
  .card__company {
    font-size: 30px;
    font-weight: 400;
    letter-spacing: 0.5px;
  }
  .card__tagline {
    font-size: 19px;
    letter-spacing: 0.5px;
  }
  .contact {
    position: absolute;
    right: 40px;
    top: 200px;
    list-style: none;
    text-align: right;
    font-size: 15px;
    line-height: 27px;
    letter-spacing: 1px;
  }
  .card--back .card__header {
    left: auto;
    right: 38px;
    text-align: right;
  }
  .services {
    position: absolute;
    left: 40px;
    right: 40px;
    bottom: 70px;
    font-size: 12px;
    letter-spacing: 1px;
    line-height: 20px;
    text-align: center;
  }
  .services__list {
    text-align: justify;
    text-align-last: center;
    padding: 0 20px;
  }
  .services__note {
    margin-top: 18px;
  }
</style>
</head>
<body>
  <section class="card card--front" aria-label="Card front">
    <header class="card__header">
      <h1 class="card__company">TKB Plumbing Services</h1>
      <p class="card__tagline">Plumbers, Drainers &amp; Gasfitters</p>
    </header>
    <ul class="contact">
      <li class="contact__name">Dorian Wellsby</li>
      <li class="contact__phone">04.71.59.60.83</li>
      <li class="contact__email">Info@tkbplumbingservices.com.au</li>
      <li class="contact__licence">LIC No 517483f</li>
      <li class="contact__abn">ABN No 61907354218</li>
    </ul>
  </section>

  <section class="card card--back" aria-label="Card back">
    <header class="card__header">
      <h2 class="card__company">TKB Plumbing Services</h2>
      <p class="card__tagline">Plumbers, Drainers &amp; Gasfitters</p>
    </header>
    <div class="services">
      <p class="services__list">Domestic, industrial, commercial, all new installations, renovations, sewer renewals, repairs</p>
      <p class="services__note">Fully licensed and insured</p>
    </div>
  </section>
</body>
</html>
```